6 - 8 'Holistic' Instagram Graphics

Hi there!
We are looking to build up a library of Graphic Templates to use as Instagram & Facebook posts for our Holistic Medi Spa (& 3 other companies eventually)
This competition is for a sample of 6 - 8 designs. For the winner(s), we will make an agreement for a batch order (Looking for 200+ designs in total), and will be looking to make a long term arrangement.
Please find a full job description in the attached Word Document.
Any questions, don't hesitate to ask.
Thanks!
Medical Spa

```html
<!DOCTYPE html>
<html lang="en">
<head>
<meta charset="utf-8">
<title>EMS Body Sculpting – LumaGrove</title>
<link href="https://fonts.googleapis.com/css2?family=Comic+Neue:wght@700&family=Ubuntu:wght@500&display=swap" rel="stylesheet">
<style>
  :root {
    --paper: #ffffff;
    --teal: #8fd4cc;
    --coral: #ee8574;
    --ink: #2a2a2a;
    --stone: #b3b1a6;
    --stone-dark: #9d9b90;
    --peach: #eccbb4;
    --cocoa: #8a5a4c;
    --photo-light: #e9e6e8;
    --photo-mid: #c9c3c6;
  }
  * { margin: 0; padding: 0; box-sizing: border-box; }
  html, body { width: 1200px; height: 1200px; overflow: hidden; background: var(--paper); }
  .post { position: relative; width: 1200px; height: 1200px; background: var(--paper); overflow: hidden; }
  .shapes { position: absolute; inset: 0; }
  .brand {
    position: absolute; left: 72px; top: 86px;
    display: flex; align-items: center; gap: 18px;
    font-family: "Ubuntu", sans-serif; font-weight: 500;
    font-size: 58px; color: var(--stone-dark); letter-spacing: 0.5px;
  }
  .brand-dot { width: 62px; height: 62px; border-radius: 50%; background: var(--stone); }
  .headline {
    position: absolute; left: 68px; top: 306px;
    font-family: "Comic Neue", cursive; font-weight: 700;
    font-size: 54px; line-height: 61px; color: var(--coral);
    word-spacing: 4px;
  }
  .lead {
    position: absolute; left: 68px; top: 646px; width: 400px;
    font-family: "Ubuntu", sans-serif; font-weight: 500;
    font-size: 19.5px; line-height: 27px; color: var(--ink);
  }
  .site-button {
    position: absolute; left: 70px; top: 888px; width: 349px; height: 71px;
    border-radius: 14px; background: var(--stone);
    display: flex; align-items: center; justify-content: center;
    font-family: "Ubuntu", sans-serif; font-weight: 500;
    font-size: 27px; color: var(--ink); letter-spacing: 0.3px;
  }
</style>
</head>
<body>
<main class="post">
  <svg class="shapes" width="1200" height="1200" viewBox="0 0 1200 1200">
    <defs>
      <linearGradient id="photoTone" x1="0" y1="0" x2="1" y2="1">
        <stop offset="0" stop-color="var(--photo-light)"/>
        <stop offset="1" stop-color="var(--photo-mid)"/>
      </linearGradient>
      <radialGradient id="floralTone">
        <stop offset="0" stop-color="var(--stone)" stop-opacity="0.35"/>
        <stop offset="1" stop-color="var(--stone)" stop-opacity="0"/>
      </radialGradient>
      <radialGradient id="sprigTone">
        <stop offset="0" stop-color="var(--peach)" stop-opacity="0.6"/>
        <stop offset="1" stop-color="var(--peach)" stop-opacity="0"/>
      </radialGradient>
    </defs>

    <path class="blob-top" fill="var(--teal)"
      d="M1014 0 H1200 V287 C1178 250 1168 185 1152 142 C1132 96 1092 110 1060 100 C1022 86 1008 42 1014 0 Z"/>
    <path class="blob-bottom" fill="var(--teal)"
      d="M0 1007 C58 1010 76 1040 68 1072 C60 1112 56 1150 120 1170 C172 1181 228 1188 254 1200 H0 Z"/>

    <rect class="dot-band dot-band-top" role="img" aria-label="Decorative grid of small peach dots"
      x="394" y="234" width="183" height="22" rx="11" fill="var(--peach)" opacity="0.35"/>
    <rect class="dot-band dot-band-bottom" role="img" aria-label="Decorative grid of small peach dots"
      x="66" y="802" width="185" height="24" rx="12" fill="var(--peach)" opacity="0.35"/>

    <ellipse class="flower flower-top" role="img" aria-label="Outlined four-petal flower ornament"
      cx="1003" cy="125" rx="70" ry="75" fill="url(#floralTone)"/>
    <ellipse class="flower flower-bottom" role="img" aria-label="Outlined four-petal flower ornament"
      cx="527" cy="1025" rx="73" ry="79" fill="url(#floralTone)"/>
    <ellipse class="sprig" role="img" aria-label="Peach leafy sprig ornament"
      cx="1100" cy="1095" rx="55" ry="98" fill="url(#sprigTone)"/>

    <g class="sparkles" fill="var(--cocoa)">
      <rect x="916" y="300" width="6" height="6" transform="rotate(45 919 303)"/>
      <rect x="960" y="311" width="10" height="10" transform="rotate(45 965 316)"/>
      <rect x="1021" y="361" width="10" height="10" transform="rotate(45 1026 366)"/>
      <rect x="734" y="1068" width="7" height="7" transform="rotate(45 737 1071)"/>
      <rect x="779" y="1093" width="12" height="12" transform="rotate(45 785 1099)"/>
      <rect x="770" y="1142" width="8" height="8" transform="rotate(45 774 1146)"/>
    </g>

    <circle class="photo-ring" cx="836" cy="716" r="330" fill="var(--stone)"/>
    <circle class="photo-gap" cx="858" cy="704" r="330" fill="var(--paper)"/>
    <circle class="photo" role="img" aria-label="Photo of an aesthetician in a white coat treating a client's face in a bright clinic room"
      cx="865" cy="704" r="323" fill="url(#photoTone)"/>
  </svg>

  <div class="brand"><span class="brand-dot"></span>LumaGrove</div>

  <h1 class="headline">EMS Body<br>Sculpting<br>is equivalent to<br>16 weeks HIT<br>Training</h1>

  <p class="lead">Radiofrequency (RF) is a highly effective method for skin tightening, reducing cellulite &amp; body reshaping.</p>

  <div class="site-button">www.lumagrove.com</div>
</main>
</body>
</html>
```